Build Steady Practice Growth Through Trust

Design a cover for this book which is designed to help a business go from it's current revenue and treatment acceptance to double (2X) that success and those metrics.

```html
<!DOCTYPE html>
<html lang="en">
<head>
<meta charset="utf-8">
<title>Build Steady Practice Growth Through Trust — Book Cover</title>
<link href="https://fonts.googleapis.com/css2?family=Archivo+Black&family=Raleway:wght@300&family=Yellowtail&display=swap" rel="stylesheet">
<style>
  :root {
    --backdrop: #e7e7e7;
    --cover-blue: #0b4a92;
    --cover-blue-deep: #083d7c;
    --accent-yellow: #eecf0c;
    --title-white: #f4f4f4;
  }
  * { margin: 0; padding: 0; box-sizing: border-box; }
  html, body {
    width: 1200px;
    height: 864px;
    overflow: hidden;
    background: var(--backdrop);
  }
  .canvas {
    position: relative;
    width: 1200px;
    height: 864px;
  }
  .book-cover {
    position: absolute;
    left: 300px;
    top: 12px;
    width: 600px;
    height: 840px;
    background: linear-gradient(160deg, var(--cover-blue) 0%, var(--cover-blue-deep) 100%);
    overflow: hidden;
  }
  .title-frame {
    position: absolute;
    left: 70px;
    top: 215px;
    width: 460px;
    height: 420px;
    border: 7px solid var(--accent-yellow);
  }
  .title-lead {
    position: absolute;
    left: 0;
    right: 0;
    top: 120px;
    text-align: center;
    font-family: "Archivo Black", sans-serif;
    font-size: 112px;
    line-height: 1;
    color: var(--accent-yellow);
  }
  .title-lead span {
    background: var(--cover-blue);
    padding: 0 18px;
  }
  .title-main {
    position: absolute;
    left: 0;
    right: 0;
    top: 262px;
    text-align: center;
    font-family: "Archivo Black", sans-serif;
    color: var(--title-white);
    text-transform: uppercase;
    line-height: 1.02;
  }
  .title-main .line { display: block; }
  .title-main .line-steady { font-size: 78px; }
  .title-main .line-practice { font-size: 70px; }
  .title-main .line-growth { font-size: 84px; }
  .title-script {
    position: absolute;
    left: 0;
    right: 0;
    top: 586px;
    text-align: center;
    font-family: "Yellowtail", cursive;
    font-size: 72px;
    line-height: 1;
    color: var(--accent-yellow);
  }
  .title-script span {
    background: var(--cover-blue-deep);
    padding: 0 14px;
  }
  .author-name {
    position: absolute;
    left: 0;
    right: 0;
    bottom: 70px;
    text-align: center;
    font-family: "Raleway", sans-serif;
    font-weight: 300;
    font-size: 34px;
    letter-spacing: 0.32em;
    color: var(--title-white);
    text-transform: uppercase;
  }
</style>
</head>
<body>
  <div class="canvas">
    <div class="book-cover">
      <div class="title-frame"></div>
      <h1 class="book-title">
        <span class="title-lead"><span>BUILD</span></span>
        <span class="title-main">
          <span class="line line-steady">Steady</span>
          <span class="line line-practice">Practice</span>
          <span class="line line-growth">Growth</span>
        </span>
        <span class="title-script"><span>Through Trust</span></span>
      </h1>
      <p class="author-name">Martin L. Hale, DDS</p>
    </div>
  </div>
</body>
</html>
```